cartNest - a stylish trolley for apartments

We neede a simple website to sell our Trolley, for apartment use.
The colour theme is red, blask & white. Our logo is attached and this needs to be on the Home page.
The website only needs a Home Page plus 4 other pges.
In the attachment you will find a site map.

You can check out the following two sites to see what I like:
www.plinvex.example/design-showcase-inspiration/minimalist-portfolio-website/
www.brostaquill.example/inspiration/40-beautiful-web-design-portfolios/ in this site especially
Dario Pesqueta
Q L Smithy
Nine 86 Studio
Albert Crisp

And especially Lamp - I ike the simpicity of the site esp as we are only selling one product

Target Market(s)

Apartment dwellers

Industry/Entity Type

Apartment

Requirements
Must have
• This website must have 4 pages.
We need Zanto, Fundline and Quibpay portals.
Order Form for Trolley
Payment form.

```html
<!DOCTYPE html>
<html lang="en">
<head>
<meta charset="utf-8">
<title>cartNest – Home</title>
<link href="https://fonts.googleapis.com/css2?family=Open+Sans:wght@400;600;700&family=Arimo:wght@700&family=Roboto+Condensed:wght@700&family=Courgette&display=swap" rel="stylesheet">
<style>
:root{
  --black:#050505;
  --red:#a30006;
  --red-bright:#e3000f;
  --red-fold:#3a0a0a;
  --panel:rgba(245,245,245,.9);
  --panel-dark:rgba(12,12,12,.82);
  --text:#333;
  --text-light:#e6e6e6;
  --white:#fff;
  --link:#0a4bd6;
}
*{box-sizing:border-box;margin:0;padding:0}
html,body{width:1200px;height:980px;overflow:hidden}
body{position:relative;background:var(--black);font-family:"Open Sans",sans-serif;color:var(--text)}
.backdrop{position:absolute;left:0;top:146px;width:1200px;height:834px;
  background:radial-gradient(ellipse at 50% 40%,#d9d6c9 0%,#a9a595 30%,#6e6a60 60%,#3a3834 100%)}
.site-header{position:absolute;left:0;top:0;width:1200px;height:146px;background:var(--black)}
.brand{position:absolute;left:158px;top:96px;display:flex;align-items:center;gap:8px;color:var(--white);font-weight:700;font-size:22px}
.brand-dot{width:14px;height:14px;border-radius:50%;background:var(--red-bright)}
.top-nav{position:absolute;right:130px;top:21px;font-size:12.5px;color:#ddd;display:flex;align-items:center;gap:8px}
.top-nav .sep{color:#777}
.top-nav svg{vertical-align:-4px;margin-right:4px}
.search{position:absolute;left:462px;top:72px;display:flex;gap:9px}
.search-field{width:220px;height:28px;border:0;border-radius:4px;background:linear-gradient(#fff,#e5e5e5)}
.search-btn{width:80px;height:28px;border:0;border-radius:4px;background:linear-gradient(#555,#2a2a2a);color:#fff;font:600 14px "Open Sans",sans-serif}
.search-links{position:absolute;left:599px;top:109px;font-size:12px;color:#ccc}
.mini-cart{position:absolute;left:804px;top:60px}
.mini-cart-title{position:absolute;left:85px;top:-2px;font-family:"Courgette",cursive;font-size:28px;color:#fff;white-space:nowrap}
.mini-cart-total{position:absolute;left:85px;top:44px;font-size:14px;font-weight:700;color:#fff;white-space:nowrap}
.mini-cart-total span{color:var(--red-bright)}
.panel{position:absolute;background:var(--panel);border-radius:4px}
.panel-dark{background:var(--panel-dark);border-radius:8px}
.ribbon{position:absolute;left:-16px;width:168px;height:56px;background:var(--red);color:#fff;
  font:700 20px "Arimo",sans-serif;display:flex;align-items:center;justify-content:center}
.ribbon::before{content:"";position:absolute;left:0;top:-16px;border-right:16px solid var(--red-fold);border-top:16px solid transparent}
.ribbon em{font-style:normal;color:var(--red-bright)}
.ribbon-order{left:-16px}
.thumbs{position:absolute;left:178px;top:20px;display:flex;gap:23px}
.thumb{width:80px;height:72px;border:3px solid #fff;box-shadow:0 0 2px #888;background:linear-gradient(#8c8a82,#4b4a45)}
.intro{position:absolute;left:178px;top:102px;width:345px;font-size:12.5px;line-height:20px}
.more-link{color:var(--red);font-weight:700}
.gallery{position:absolute;left:177px;top:22px;display:grid;grid-template-columns:158px 158px;gap:20px 22px}
.product{height:97px;background:#fff;border:1px solid #ccc;position:relative}
.product-img{position:absolute;left:20px;top:10px;width:62px;height:78px;border-radius:6px;background:linear-gradient(#cfcfcf,#8d8d8d)}
.price{position:absolute;left:95px;top:26px;font:700 22px "Roboto Condensed",sans-serif;color:var(--red)}
.details{position:absolute;left:99px;top:64px;font-size:13px;color:#333}
.welcome h1{position:absolute;left:25px;top:14px;font:700 26px "Arimo",sans-serif;color:#e8e8e8}
.welcome h1 span,.red{color:var(--red-bright)}
.welcome p{position:absolute;left:26px;top:60px;width:340px;font-size:13.3px;line-height:25px;color:var(--text-light)}
.welcome b{color:#fff}
.btn-more{position:absolute;left:145px;top:446px;width:91px;height:36px;border-radius:4px;background:#fff;color:var(--red-bright);font-size:17px;display:flex;align-items:center;justify-content:center}
.address{position:absolute;left:178px;top:16px;font-size:12.5px;line-height:22.5px}
.address h2{font-size:16px;font-weight:700;color:#222;line-height:22px}
.address h3{font-size:14px;font-weight:700;color:#222}
.address .label{color:var(--red-bright);font-weight:700}
.address a{color:var(--link)}
.address .phone{font-weight:700;color:#111}
.order-form{position:absolute;left:173px;top:16px;width:259px}
.field{height:27px;border:1px solid #bbb;border-radius:5px;background:linear-gradient(#fff,#e8e8e8);font-size:12px;color:#888;padding:4px 14px;margin-bottom:7px}
.row{display:flex;gap:8px}
.row .field{flex:1}
.select{position:relative;padding-right:30px}
.select::after{content:"";position:absolute;right:0;top:0;width:26px;height:25px;background:linear-gradient(#eee,#ccc);border-left:1px solid #aaa;border-radius:0 5px 5px 0}
.select::before{content:"";position:absolute;right:7px;top:10px;z-index:1;border:6px solid transparent;border-top:6px solid #333;border-bottom:0}
.submit{display:block;margin:6px auto 0;width:100px;height:25px;border-radius:4px;background:linear-gradient(#555,#222);color:#fff;font-size:12.5px;text-align:center;line-height:25px}
.site-footer{position:absolute;left:130px;top:901px;width:940px;height:69px;background:var(--black);border-radius:4px}
.copyright{position:absolute;left:17px;top:25px;font-size:12.5px;color:#ccc}
.payments{position:absolute;left:689px;top:21px;display:flex;gap:1px}
.pay{width:45px;height:28px;background:#f2f2f2;border:1px solid #999;font-size:9px;font-weight:700;color:#333;display:flex;align-items:center;justify-content:center;text-align:center;line-height:10px}
</style>
</head>
<body>
<div class="backdrop" role="img" aria-label="Blurred photo of a hotel lobby with a luggage trolley"></div>

<header class="site-header">
  <div class="brand"><span class="brand-dot"></span>cartNest</div>
  <nav class="top-nav">
    <span>Sign in or Create an account</span><span class="sep">|</span>
    <span><svg width="22" height="18" viewBox="0 0 22 18" fill="none" stroke="#ddd" stroke-width="1.5"><path d="M1 2h3l3 10h11l2-7H5"/><circle cx="8" cy="15.5" r="1.5"/><circle cx="17" cy="15.5" r="1.5"/></svg>Cart</span><span class="sep">|</span>
    <span>Gift Certificates</span><span class="sep">|</span>
    <span>Wish Lists</span><span class="sep">|</span>
    <span>Order Status</span><span class="sep">|</span>
    <span>My Account</span>
  </nav>
  <form class="search"><input class="search-field" type="text" aria-label="Search"><button class="search-btn" type="button">Search</button></form>
  <div class="search-links">Advanced Search | Search Tips</div>
  <div class="mini-cart">
    <svg width="70" height="62" viewBox="0 0 70 62" fill="none" stroke="#bbb" stroke-width="3"><path d="M2 6h10l10 34h36l8-26H16"/><path d="M18 22h46M21 31h41M30 14l4 26M42 14l1 26M54 14l-2 26" stroke-width="1.5"/><circle cx="26" cy="53" r="5" fill="#222"/><circle cx="54" cy="53" r="5" fill="#222"/></svg>
    <div class="mini-cart-title">Shopping Cart</div>
    <div class="mini-cart-total"><span>Total Cart</span> $0.00 Item</div>
  </div>
</header>

<section class="panel" style="left:130px;top:176px;width:541px;height:221px">
  <div class="ribbon" style="top:83px"><em>cart</em>&nbsp;Nest</div>
  <div class="thumbs">
    <div class="thumb" role="img" aria-label="Trolley being loaded from a car"></div>
    <div class="thumb" role="img" aria-label="Trolley beside an open car boot"></div>
    <div class="thumb" role="img" aria-label="Trolley in an apartment lift"></div>
  </div>
  <p class="intro">cartNest is made of high quality stainless steel and other robust materials. Whilst other trolleys tend to look like they belong in a factory or workshop, cartNest is the classy alternative, which can live anywhere in your apartment, and not in the cupboard... <span class="more-link">More</span></p>
</section>

<section class="panel" style="left:130px;top:417px;width:541px;height:255px">
  <div class="ribbon" style="top:100px"><em>my</em>&nbsp;Gallery</div>
  <div class="gallery">
    <div class="product"><div class="product-img" role="img" aria-label="Chrome birdcage trolley"></div><span class="price">$1299</span><span class="details">Details</span></div>
    <div class="product"><div class="product-img" role="img" aria-label="Bronze birdcage trolley"></div><span class="price">$1459</span><span class="details">Details</span></div>
    <div class="product"><div class="product-img" role="img" aria-label="Angled frame trolley"></div><span class="price">$1209</span><span class="details">Details</span></div>
    <div class="product"><div class="product-img" role="img" aria-label="Brass trolley with black base"></div><span class="price">$1800</span><span class="details">Details</span></div>
  </div>
</section>

<section class="panel panel-dark welcome" style="left:690px;top:176px;width:380px;height:496px">
  <h1>Welcome to <span>cart</span>Nest</h1>
  <p><b><span class="red">cart</span>Nest</b> evolved from demand! Apartment dwellers everywhere are calling for a solution to moving shopping, luggage and other goods from car to apartment, and vice versa. Other trolleys on the market are not versatile, they are not robust, but more importantly, they are NOT stylish! The emphasis of cartNest is on style. This trolley is stylish enough to remain in your apartment as a piece of furniture. It features a versatile flat-bed and hanger, to cope with all your transport needs.<br>IT LOOKS GREAT! Designed along the lines of the familiar hotel “birdcage” luggage trolley, it provides smart and practical use for all small transport needs. The stylish trolley does not need to be disassembled and stored away in a cupboard or storage area.</p>
  <span class="btn-more">More</span>
</section>

<section class="panel" style="left:130px;top:690px;width:461px;height:195px">
  <div class="ribbon" style="top:70px"><em>my</em>&nbsp;Contact</div>
  <address class="address" style="font-style:normal">
    <h2>Our Address :</h2>
    <h3><span class="red">cart</span>Nest</h3>
    Nestworks Trading Ltd.<br>4127 Halvern<br>Lane,Glasgow, G07 31KQ.<br>
    <span class="label">Email :</span> <a href="#">hello@cartnest.example</a><br>
    <span class="label">Phone No :</span> <span class="phone">555 218 4370,&nbsp; 555 309 6612</span>
  </address>
</section>

<section class="panel" style="left:616px;top:690px;width:455px;height:195px">
  <div class="ribbon ribbon-order" style="top:70px"><em>Send</em>&nbsp;Order</div>
  <div class="order-form">
    <div class="field">Full Name</div>
    <div class="field">Postal Address</div>
    <div class="row"><div class="field">Email</div><div class="field">Phone.</div></div>
    <div class="row"><div class="field select">Products</div><div class="field select">Select Range</div></div>
    <span class="submit">Submit Order</span>
  </div>
</section>

<footer class="site-footer">
  <div class="copyright">Copyright © 2012 <span class="red">cart</span>Nest. All Right Reserved &nbsp;|&nbsp; Privacy Policy</div>
  <div class="payments">
    <span class="pay">Fundline</span><span class="pay">Zanto</span><span class="pay">Ewirra</span><span class="pay">Quibpay</span><span class="pay">Direct Deposit</span>
  </div>
</footer>
</body>
</html>
```